Environmental Plastics Infographic on Marine Debris

We need a series of infographics that can be used individually or as a combined presentation. We'd like the combined piece to include an introduction and conclusion along with 4-5 infographics. Each infographic (information unit) should also work as a standalone. We are trying to help people visualize size proportions and ratios to put the plastics marine debris problem in perspective. Our key point is concerning polystyrene foam which represents 35 tons. We are looking for something creative to help people understand what the problem represents in terms they are familiar with.

To view our typical company design/style please see our website at www.brantleyfoamworks.org. Our primary RGB colors are: (187,140,9); (94,47,29); (94,138,164); and (164,167,15). Secondary RGB colors are (249,162,28) and (218,210,208). Our title/header font is DIN Next LT Pro and our copy font is Calibri 10.5 pt. We can deviate from the font specification if beneficial and welcome interesting text treatments and typography.

Need extra days to review

Target Market(s)

international brand manufacturers (corvantel, makiro), US legislators & government agencies

Font styles to use
Sans Serif

Requirements
Must have
• Sufficient white space. Easy to grasp message concept with visual components.

```html
<!DOCTYPE html>
<html lang="en">
<head>
<meta charset="utf-8">
<title>Will Polystyrene Bans Improve Ocean Health</title>
<link rel="stylesheet" href="https://fonts.googleapis.com/css2?family=Montserrat:wght@700;800;900&family=Source+Sans+3:ital,wght@0,400;0,600;0,700;1,400&display=swap">
<style>
:root{
  --steel:#5e8aa4;
  --steel-dark:#46718f;
  --steel-pale:#dfe7ed;
  --gold:#bb8c09;
  --olive:#a4a70f;
  --olive-pale:#eff0d8;
  --brown:#5e2f1d;
  --orange:#f9a21c;
  --stone:#dad2d0;
  --ink:#2e3338;
  --grey:#7d858c;
  --panel:#f1f2f3;
}
*{box-sizing:border-box;margin:0;padding:0}
html,body{width:927px;height:1200px;overflow:hidden;background:#fff}
body{position:relative;font-family:"Source Sans 3",sans-serif;color:var(--ink)}
.abs{position:absolute}
.display{font-family:"Montserrat",sans-serif;font-weight:900;letter-spacing:-.3px}

/* header */
.masthead{left:0;top:0;width:927px;height:104px;background:linear-gradient(112deg,#e7f0de 0 72%,#dde5ed 72%)}
.masthead h1{position:absolute;left:0;right:0;top:44px;text-align:center;font-size:31px;color:#2f2f2f;transform:scaleX(.97)}
.wave-art{left:0;top:118px;width:440px;height:174px;background:linear-gradient(180deg,#a9c4d8 0%,#6d9cbd 55%,#cfdde8 100%);border-radius:0 120px 0 0}
.intro{left:484px;top:164px;width:362px;font-size:15.2px;line-height:20px;color:#444}
.lead{left:51px;top:306px;font-size:14.6px;color:#333}
.lead b{color:var(--steel);font-weight:600;font-size:17px}

.panel{position:absolute;overflow:hidden}

/* weight tags */
.weight{display:inline-flex;flex-direction:column;align-items:center;vertical-align:top}
.weight::before{content:"";width:9px;height:5px;border:2px solid var(--steel-dark);border-bottom:none;border-radius:5px 5px 0 0}
.weight span{display:flex;align-items:center;justify-content:center;text-align:center;background:var(--steel-dark);color:#fff;font-weight:700;clip-path:polygon(12% 0,88% 0,100% 100%,0 100%);line-height:1}
.w-md span{width:38px;height:32px;font-size:9px}
.w-sm span{width:24px;height:20px;font-size:6px}
.w-sm::before{width:6px;height:4px;border-width:1.5px}

/* panel 1 */
.p-mass{left:25px;top:338px;width:459px;height:264px;background:var(--steel-pale)}
.mass-label{left:18px;top:40px;width:118px;font-size:14px;line-height:18px;color:var(--grey)}
.mass-value{left:20px;top:101px;font-size:23px;font-weight:700;color:#333}
.mass-value small,.tons{font-size:10px;font-weight:700}
.scale-art{left:28px;top:128px;width:92px;height:94px;background:var(--steel);border-radius:8px 8px 12px 12px}
.divider-v{left:147px;top:26px;height:208px;border-left:1.5px dashed #555}
.pct-big{font-size:25px;font-weight:700;color:var(--steel)}
.note{font-size:10.5px;line-height:14.5px;color:var(--grey)}
.note b{font-weight:600;color:var(--steel)}
.icon-art{background:#b9cbd8;border-radius:6px}

/* panel 2 */
.p-size{left:502px;top:338px;width:401px;height:264px;background:var(--panel)}
.size-title{left:0;right:0;top:16px;text-align:center;font-size:19px;color:#333}
.size-col{top:44px;height:162px}
.size-col h3{position:relative;z-index:1;height:27px;background:#a5b8c8;font-size:10.5px;font-weight:600;text-align:center;line-height:27px;color:#222;white-space:nowrap}
.size-col .range{position:absolute;top:82px;width:100%;text-align:center;font-size:14px;font-weight:700;color:#222}
.size-col svg{position:absolute;left:50%;transform:translateX(-50%)}
.size-col .weight{position:absolute;top:110px;left:50%;transform:translateX(-50%)}
.total-bar{left:34px;top:206px;width:322px;height:28px;background:var(--steel);color:#fff;text-align:center;font-size:13px;font-weight:600;line-height:28px}
.total-bar b{font-size:17px;font-weight:700;margin:0 3px}

/* panel 3 */
.p-big{left:25px;top:620px;width:459px;height:394px;background:var(--panel)}
.big-title{left:0;right:0;top:8px;text-align:center;font-size:25px;color:#333}
.compare{left:17px;top:42px;width:424px;height:74px;background:#d7e0e8;overflow:hidden}
.compare .label{font-size:13px;color:#333}
.compare .value{font-size:21px;font-weight:600;color:#222}
.frame{left:15px;top:126px;width:430px;height:257px;background:#b7bbbe;padding:8px}
.col{position:absolute;top:8px;height:241px;text-align:center}
.col h4{margin-top:16px;font-size:16.5px;font-weight:600}
.col .art{margin:12px auto 0;height:74px;border-radius:6px}
.col .count{font-size:13px;font-weight:700;margin-top:8px}
.col .what{font-size:9.5px;text-transform:uppercase;margin-top:1px}
.col .amount{display:inline-block;margin-top:5px;background:#5a5a5a;color:#fff;font-size:15px;font-weight:600;padding:1px 6px}
.col .amount small{font-size:10px}
.col .stack{margin-top:8px;display:flex;justify-content:center;gap:6px;flex-wrap:wrap}
.col-ship{left:8px;width:120px;background:#e2d8d5;color:#333}
.col-whale{left:128px;width:140px;background:#6f96b3;color:#fff}
.col-whale .amount{background:#3e4347}
.col-city{left:268px;width:154px;background:#e6dcd8;color:#333}

/* panel 4 */
.p-eps{left:502px;top:618px;width:401px;height:278px;background:var(--panel)}
.eps-title{left:0;right:0;top:11px;text-align:center;font-size:13.2px;font-weight:800;color:#333}
.eps-box{background:#fff;border:2px solid var(--olive);box-shadow:3px 3px 0 #c7c8b8}
.eps-big{font-size:19px;font-weight:600}
.eps-big small{font-size:8px}
.eps-desc{font-size:11px;line-height:14px;color:#333}
.dash-box{border:1.3px dashed var(--steel)}
.tiny{font-size:7px;line-height:9px;color:#444}

/* panel 5 */
.p-find{left:502px;top:914px;width:401px;height:266px;background:var(--panel)}
.find-title{left:0;right:0;top:14px;text-align:center;font-size:19.5px;color:#333}
.find-text{font-size:11px;line-height:14.5px;color:#444}
.find-text b{font-weight:600}
.aside{left:256px;top:58px;width:145px;height:208px;background:#dbe2e8;padding:6px 6px 0 14px;font-size:12px;line-height:16.3px;color:#333}
.aside b{color:var(--gold);font-weight:600}
.aside em{font-style:normal;color:var(--steel);font-weight:600}

/* panel 6 */
.p-cars{left:25px;top:1032px;width:459px;height:148px;background:linear-gradient(120deg,#e9ecef 0 62%,#f3f4f5 62%)}
.cars-small{font-size:10px;color:#222}
.cars-big{font-size:20px;font-weight:700;color:#111}
.cars-rule{left:32px;top:61px;width:203px;border-top:1.5px dashed #555}
.news-card{left:257px;top:8px;width:172px;height:146px;background:#fff;transform:rotate(-5deg);box-shadow:0 1px 4px rgba(0,0,0,.15);padding:8px 10px}
.news-brand{font-size:13px;font-weight:700;color:#222;display:flex;align-items:center;gap:4px}
.news-brand i{width:11px;height:11px;border-radius:50%;background:#222;display:inline-block}
.news-photo{margin-top:5px;height:62px;background:linear-gradient(180deg,#7fa3c8,#3a5f8a)}
.news-head{margin-top:4px;font-family:Georgia,serif;font-size:9.5px;line-height:10.5px;font-weight:700;color:#111}
.news-date{font-size:4.5px;color:#777;text-align:right}
</style>
</head>
<body>

<header class="abs masthead"><h1 class="display">WILL POLYSTRENE BANS IMPROVE OCEAN HEALTH</h1></header>

<div class="abs wave-art" role="img" aria-label="Illustration of a breaking ocean wave with plastic debris floating on the surface and a school of fish below"></div>
<p class="abs intro">A recent report looks at the role plastics play in marine debris in the Great Pacific Garbage Patch (GPGP) that sheds light on previous assumptions about how different plastics contribute to the problem and where its coming from.</p>
<p class="abs lead">Polystyrene ban legislation imply product restrictions will minimize plastic marine debris. <b>Let’s Take A Closer Look</b>.</p>

<!-- Total mass -->
<section class="panel p-mass">
  <p class="abs mass-label">The total plastics mass in the GPGP is projected at</p>
  <p class="abs mass-value">78,908 <small>TONS</small></p>
  <div class="abs scale-art" role="img" aria-label="Weighing scale icon with dial"></div>
  <div class="abs divider-v"></div>

  <div class="abs icon-art" style="left:252px;top:2px;width:52px;height:24px" role="img" aria-label="Foam food tray icon"></div>
  <p class="abs" style="left:259px;top:38px;font-size:18px;font-weight:700">0.05%</p>
  <p class="abs note" style="left:315px;top:26px;width:140px">is <b>FOAMED PLASTICS</b> – including polystyrene – making it a minor component of the GPGP.</p>

  <p class="abs pct-big" style="left:167px;top:95px">52%</p>
  <svg class="abs" style="left:190px;top:70px" width="78" height="22"><polyline points="1,22 1,1 76,1" fill="none" stroke="#777" stroke-width="1"/></svg>
  <p class="abs note" style="left:170px;top:127px;width:68px;font-size:10px;line-height:13.5px">Mostly <b>ABANDONED FISHING GEAR</b>, not consumer plastics.</p>
  <div class="abs icon-art" style="left:164px;top:196px;width:90px;height:42px" role="img" aria-label="Fishing net, fish and hook icons"></div>

  <svg class="abs" style="left:239px;top:74px" width="96" height="96" viewBox="0 0 96 96">
    <circle cx="48" cy="48" r="31" fill="none" stroke="var(--steel)" stroke-width="34"/>
    <circle cx="48" cy="48" r="31" fill="none" stroke="var(--gold)" stroke-width="34" stroke-dasharray="91.6 200" transform="rotate(-90 48 48)"/>
    <circle cx="48" cy="48" r="14" fill="#fff"/>
    <text x="5" y="40" fill="#fff" font-size="15" font-weight="700" font-family="Source Sans 3,sans-serif">52%</text>
    <text x="67" y="61" fill="#fff" font-size="12" font-weight="700" font-family="Source Sans 3,sans-serif">47%</text>
  </svg>

  <div class="abs icon-art" style="left:347px;top:82px;width:88px;height:56px" role="img" aria-label="Film reel and pipe icons"></div>
  <p class="abs pct-big" style="left:347px;top:138px">47%</p>
  <p class="abs note" style="left:317px;top:173px;width:140px">is <b>HARD PLASTICS</b>, <b>SHEETS</b> and <b>FILM</b>, making up the majority of the microplastics mass</p>
</section>

<!-- Sizing it up -->
<section class="panel p-size">
  <h2 class="abs display size-title">SIZING IT UP</h2>

  <div class="abs size-col" style="left:13px;width:83px;background:#ebebeb">
    <h3>MICROPLASTICS</h3>
    <svg style="top:60px" width="14" height="12" viewBox="0 0 14 12"><polygon points="7,1 13,4 7,7 1,4" fill="#777"/><polygon points="1,4 7,7 7,11 1,8" fill="#444"/><polygon points="13,4 7,7 7,11 13,8" fill="#555"/></svg>
    <p class="range">0.05-0.5cm</p>
    <div class="weight w-md"><span>6.5K<br>TONS</span></div>
  </div>
  <div class="abs size-col" style="left:99px;width:80px;background:var(--olive-pale)">
    <h3>MESOPLASTICS</h3>
    <svg style="top:56px" width="22" height="18" viewBox="0 0 22 18"><polygon points="11,1 21,6 11,11 1,6" fill="#b8bb2a"/><polygon points="1,6 11,11 11,17 1,12" fill="#7d7f10"/><polygon points="21,6 11,11 11,17 21,12" fill="#949612"/></svg>
    <p class="range">0.5-5cm</p>
    <div class="weight w-md"><span>10K<br>TONS</span></div>
  </div>
  <div class="abs size-col" style="left:183px;width:98px;background:#ebebeb">
    <h3>MACROPLASTICS</h3>
    <svg style="top:48px" width="32" height="26" viewBox="0 0 32 26"><polygon points="16,1 31,8 16,15 1,8" fill="#888"/><polygon points="1,8 16,15 16,25 1,18" fill="#444"/><polygon points="31,8 16,15 16,25 31,18" fill="#5f5f5f"/></svg>
    <p class="range">5-50cm</p>
    <div class="weight w-md"><span>20K<br>TONS</span></div>
  </div>
  <div class="abs size-col" style="left:284px;width:103px;background:var(--olive-pale)">
    <h3>MEGAPLASTICS</h3>
    <svg style="top:33px" width="52" height="42" viewBox="0 0 54 44"><polygon points="27,1 53,13 27,25 1,13" fill="#c4c73c"/><polygon points="1,13 27,25 27,43 1,31" fill="#7d7f10"/><polygon points="53,13 27,25 27,43 53,31" fill="#9a9c12"/></svg>
    <p class="range">&gt;50cm</p>
    <div class="weight w-md"><span>42K<br>TONS</span></div>
  </div>
  <div class="abs total-bar">TOTAL GPGP <b>78,9K</b> <span class="tons">TONS</span></div>
</section>

<!-- How big is big -->
<section class="panel p-big">
  <h2 class="abs display big-title">HOW BIG IS BIG?</h2>
  <div class="abs compare">
    <p class="abs label" style="left:22px;top:9px">ALL GDP PLASTICS</p>
    <p class="abs value" style="left:21px;top:28px">78,908 <span class="tons">TONS</span></p>
    <div class="abs weight w-md" style="left:158px;top:19px"><span>50K<br>TONS</span></div>
    <div class="abs" style="left:203px;top:19px;width:26px;overflow:hidden"><div class="weight w-md"><span>50K<br>TONS</span></div></div>
    <div class="abs" style="left:232px;top:14px;height:48px;border-left:1px solid #8a96a0"></div>
    <p class="abs label" style="left:248px;top:9px">All Foam Plastics</p>
    <p class="abs value" style="left:248px;top:28px">35 tons</p>
    <div class="abs" style="left:386px;top:19px;width:22px;overflow:hidden"><div class="weight w-md"><span>50K<br>TONS</span></div></div>
  </div>

  <div class="abs frame">
    <div class="col col-ship">
      <h4>GPGP = 79%</h4>
      <div class="art" style="width:96px;background:#9c9494" role="img" aria-label="Cruise ship illustration"></div>
      <p class="count">1</p><p class="what">Cruise ship</p>
      <p class="amount">100,000 <small>TONS</small></p>
      <div class="stack"><div class="weight w-md"><span>50K<br>TONS</span></div><div class="weight w-md"><span>50K<br>TONS</span></div></div>
    </div>
    <div class="col col-whale">
      <h4>GPGP = 53%</h4>
      <div class="art" style="width:110px;background:#3f6d8f" role="img" aria-label="Blue whale illustration"></div>
      <p class="count">1</p><p class="what" style="font-size:13px">Blue whale</p>
      <p class="amount">150,000 <small>TONS</small></p>
      <div class="stack"><div class="weight w-md"><span>50K<br>TONS</span></div><div class="weight w-md"><span>50K<br>TONS</span></div><div class="weight w-md"><span>50K<br>TONS</span></div></div>
    </div>
    <div class="col col-city">
      <h4>GPGP = 29%</h4>
      <div class="art" style="width:140px;background:#8f8a89" role="img" aria-label="City skyline with a garbage truck illustration"></div>
      <p class="count">1 WEEK</p><p class="what">NYC waste generation</p>
      <p class="amount">269,230 <small>TONS</small></p>
      <div class="stack" style="gap:4px"><div class="weight w-sm"><span>50K<br>TONS</span></div><div class="weight w-sm"><span>50K<br>TONS</span></div><div class="weight w-sm"><span>50K<br>TONS</span></div><div class="weight w-sm"><span>50K<br>TONS</span></div><div class="weight w-sm"><span>50K<br>TONS</span></div></div>
      <div style="position:absolute;left:22px;top:218px;width:6px;height:14px;background:var(--steel-dark)"></div>
    </div>
  </div>
</section>

<!-- Mismanaged EPS -->
<section class="panel p-eps">
  <h2 class="abs display eps-title">HOW MUCH MISMANAGED EPS WASTE WAS FOUND?</h2>

  <div class="abs eps-box" style="left:202px;top:48px;width:162px;height:194px">
    <p class="abs eps-big" style="left:21px;top:10px;color:var(--brown)">6,620,000 <small>TONS</small></p>
    <p class="abs eps-desc" style="left:23px;top:34px;width:120px;font-size:10px;line-height:13px">Worldwide Expanded Polystyrene (EPS) Plastics Production</p>
    <div class="abs dash-box" style="left:21px;top:80px;width:86px;height:90px;border-color:var(--orange)">
      <p class="abs" style="left:12px;top:10px;font-size:12px;font-weight:700;color:var(--orange)">35 <span style="font-size:6px">TONS</span></p>
      <p class="abs tiny" style="left:12px;top:25px">Total GPGP<br><span style="color:var(--orange)">Foam Plastics</span></p>
      <p class="abs" style="left:12px;top:46px;font-size:9px;font-weight:700;color:var(--orange)">0.0000053%</p>
      <p class="abs tiny" style="left:12px;top:62px">Percent of Global<br>Production in GPGP</p>
    </div>
    <svg class="abs" style="left:110px;top:84px" width="40" height="72" viewBox="0 0 40 72">
      <polygon points="2,10 20,2 38,10 20,18" fill="#e8d8d4"/>
      <polygon points="2,10 20,18 20,70 2,60" fill="#d6bfb9"/>
      <polygon points="38,10 20,18 20,70 38,60" fill="#bfa69f"/>
      <polygon points="2,48 20,56 20,70 2,60" fill="#c98a2a"/>
      <polygon points="38,48 20,56 20,70 38,60" fill="#b07315"/>
    </svg>
  </div>

  <div class="abs eps-box" style="left:29px;top:39px;width:174px;height:217px">
    <p class="abs eps-big" style="left:20px;top:17px;color:var(--olive)">320,000,000 <small>TONS</small></p>
    <p class="abs eps-desc" style="left:22px;top:40px;width:100px">Worldwide Annual Plastics Production</p>
    <div class="abs dash-box" style="left:20px;top:116px;width:90px;height:78px;border-color:var(--steel)">
      <p class="abs" style="left:8px;top:7px;font-size:12px;font-weight:700;color:var(--steel)">78,908 <span style="font-size:6px">TONS</span></p>
      <p class="abs tiny" style="left:8px;top:22px">Total GPGP Plastics</p>
      <p class="abs" style="left:8px;top:38px;font-size:10px;font-weight:700;color:var(--steel)">0.000024%</p>
      <p class="abs tiny" style="left:8px;top:53px">Percent of Global<br>Production in GPGP</p>
    </div>
    <svg class="abs" style="left:114px;top:70px" width="42" height="132" viewBox="0 0 42 132">
      <polygon points="2,10 21,2 40,10 21,18" fill="#dfe0a6"/>
      <polygon points="2,10 21,18 21,130 2,120" fill="#c6c86a"/>
      <polygon points="40,10 21,18 21,130 40,120" fill="#a9ab3a"/>
      <polygon points="2,100 21,108 21,130 2,120" fill="#6c8a3a"/>
      <polygon points="40,100 21,108 21,130 40,120" fill="#5a7a2e"/>
    </svg>
  </div>
</section>

<!-- Surprising discoveries -->
<section class="panel p-find">
  <h2 class="abs display find-title">SURPRISING DISCOVERIES</h2>
  <svg class="abs" style="left:60px;top:42px" width="130" height="116" viewBox="0 0 130 116">
    <circle cx="66" cy="56" r="33" fill="none" stroke="#e4e4e4" stroke-width="42"/>
    <circle cx="66" cy="56" r="33" fill="none" stroke="var(--olive)" stroke-width="42" stroke-dasharray="103.7 210" transform="rotate(180 66 56)"/>
    <circle cx="66" cy="56" r="33" fill="none" stroke="var(--orange)" stroke-width="42" stroke-dasharray="41.5 210"/>
    <circle cx="66" cy="56" r="12" fill="#fff"/>
    <text x="54" y="24" fill="#fff" font-size="19" font-weight="700" text-anchor="middle" font-family="Source Sans 3,sans-serif">50%</text>
    <text x="98" y="80" fill="#fff" font-size="17" font-weight="700" text-anchor="middle" font-family="Source Sans 3,sans-serif">20%</text>
    <polyline points="12,56 0,56 0,96" fill="none" stroke="var(--olive)" stroke-width="1"/>
    <polyline points="118,70 126,70 126,116" fill="none" stroke="var(--orange)" stroke-width="1"/>
  </svg>
  <p class="abs find-text" style="left:22px;top:146px;width:90px">Approximately 50% of GPGP Plastics are <b style="color:var(--olive)">From Marine-Based Sources</b>.</p>
  <p class="abs find-text" style="left:130px;top:164px;width:120px">20% of the GPGP Plastic Debris Is <b style="color:var(--orange)">From the 2011 Tohoku Tsunami</b></p>
  <p class="abs" style="left:24px;top:232px;width:230px;font-size:9.5px;line-height:12.5px;font-style:italic;color:#555"><span style="color:var(--steel)">Beach Litter</span> Studies Were Not Indicative of GPGP Content.</p>
  <div class="abs aside">All marine plastic debris is a problem! However, plastic product bans will be ineffective in reducing ocean debris, especially since the <em>U.S.</em> <b>contributes less than 1%</b> of the world's mismanaged plastic waste.</div>
</section>

<!-- Cars comparison -->
<section class="panel p-cars">
  <p class="abs cars-small" style="left:35px;top:16px">TOTAL GPGP MASS</p>
  <p class="abs cars-big" style="left:32px;top:31px">&gt;43,000 CARS</p>
  <div class="abs cars-rule"></div>
  <p class="abs cars-small" style="left:32px;top:71px;font-size:12px">TOTAL FOAM PLASTIC MASS</p>
  <p class="abs cars-big" style="left:32px;top:90px;font-size:19px">18 CARS</p>
  <div class="abs news-card">
    <p class="news-brand"><i></i>Coastline Report</p>
    <div class="news-photo" role="img" aria-label="Photograph of a research crew hauling nets from the side of a boat at sea"></div>
    <p class="news-head">Great Pacific Garbage Patch weighs more than 43,000 cars and is much larger than we thought</p>
    <p class="news-date">Mar 22, 2018 5:00 PM</p>
  </div>
</section>

</body>
</html>
```